Business Card Design Project

We need a business card to reflect the design of our website - just so it all ties in - it has a retro feel and can be found at http://www.lunetaswingduo.com
We will need our phone 0493 215 764
Web address, and email lunetaduo@corvanet.com included
Our catch cry is "Classic Cocktail Music"
Perfect Live Music for Private & Corporate Events, Weddings and Dinner Music
Our names should be included :-
Deborah Feltham / piano & Owen Lockett / bass
I am now also including our logo so that it can be included (in part or whole) somehow in the design
My partner thinks we should include our logo in some form in the design of the card - i will attach this here for you. I will attach eps but if you prefer another format please let me know
Regards
Debbie

```html
<!DOCTYPE html>
<html lang="en">
<head>
<meta charset="utf-8">
<title>Luneta Duo — Business Card</title>
<link rel="stylesheet" href="https://fonts.googleapis.com/css2?family=Oswald:wght@400;600;700&family=Josefin+Sans:wght@300;400&family=Source+Code+Pro:wght@500&family=Roboto+Slab:wght@700&display=swap">
<style>
  :root {
    --teal: #80b6b2;
    --teal-dark: #6c9f9b;
    --orange: #d8815d;
    --charcoal: #3e3e3e;
    --cream: #f1e7c9;
    --cream-shade: #c9bd99;
    --ribbon-fold: #8f8569;
    --white: #ffffff;
    --link: #e07b55;
  }
  * { box-sizing: border-box; margin: 0; padding: 0; }
  html, body { width: 1200px; height: 1000px; overflow: hidden; background: #fff; }
  .canvas { position: relative; width: 1200px; height: 1000px; }

  .card { position: absolute; left: 186px; width: 810px; background: var(--teal); overflow: hidden; }
  .card--front { top: 20px; height: 468px; }
  .card--back { top: 506px; height: 467px; }

  .stitch { position: absolute; left: 0; right: 0; border-top: 1px dashed rgba(60,90,88,.45); }

  .front-band {
    position: absolute; left: 0; right: 0; top: 93px; height: 335px;
    background: var(--orange);
  }
  .front-band .stitch { border-color: rgba(120,60,40,.35); }

  .emblem { position: absolute; border-radius: 50%; background: var(--charcoal); border: 3px solid var(--teal-dark); }
  .emblem--front { left: 356px; top: 5px; width: 92px; height: 92px; }
  .emblem-tab {
    position: absolute; left: 346px; top: 80px; width: 112px; height: 36px;
    background: var(--teal); border-radius: 0 0 56px 56px;
  }
  .emblem--back { left: 306px; top: 67px; width: 164px; height: 164px; border-width: 4px; }

  .contact-panel {
    position: absolute; left: 35px; top: 140px; width: 385px; height: 260px;
    background: var(--charcoal); color: var(--cream);
    font-family: "Source Code Pro", monospace; font-size: 13px; letter-spacing: .3px;
  }
  .contact-panel .stitch { border-color: rgba(255,255,255,.25); }
  .contact-row { position: absolute; left: 16px; display: flex; gap: 14px; align-items: flex-start; line-height: 18px; white-space: nowrap; }
  .contact-row svg { flex: none; }
  .contact-row .email { color: var(--link); }
  .site-pill {
    position: absolute; left: 145px; top: 176px; width: 76px; height: 20px; border-radius: 10px;
    background: var(--teal); color: var(--charcoal); text-align: center;
    font-family: "Roboto Slab", serif; font-weight: 700; font-size: 12px; line-height: 20px;
  }
  .site-url {
    position: absolute; left: 0; right: 0; top: 204px; text-align: center;
    font-family: "Roboto Slab", serif; font-weight: 700; font-size: 16px; letter-spacing: 3px; color: var(--white);
  }
  .site-url span { color: var(--teal); }

  .tagline {
    position: absolute; left: 426px; color: var(--white); white-space: nowrap;
    font-family: "Oswald", sans-serif; font-weight: 700; font-size: 18px; letter-spacing: -.5px;
    transform: scaleY(1.2); transform-origin: left top;
  }
  .wordmark {
    position: absolute; font-family: "Josefin Sans", sans-serif; font-weight: 300;
    color: var(--cream); white-space: nowrap; z-index: 2;
  }
  .wordmark--front { left: 428px; top: 236px; font-size: 37px; letter-spacing: 1px; }
  .wordmark--back { left: 222px; top: 226px; font-size: 51px; letter-spacing: 1px; }

  .ribbon { position: absolute; z-index: 2; }
  .ribbon-text {
    position: absolute; left: 0; right: 0; text-align: center; white-space: nowrap;
    font-family: "Oswald", sans-serif; font-weight: 600; color: var(--charcoal);
    transform-origin: center center;
  }
  .members {
    position: absolute; left: 433px; top: 344px; color: var(--white); white-space: nowrap;
    font-family: "Oswald", sans-serif; font-weight: 700; font-size: 19px; line-height: 32px; letter-spacing: .5px;
  }
  .instrument-art {
    position: absolute; left: 684px; top: 200px; width: 92px; height: 218px; z-index: 1;
    background: linear-gradient(180deg, #fff 0%, #f5ede6 100%); border-radius: 36px 36px 44px 44px;
  }
</style>
</head>
<body>
<div class="canvas">

  <section class="card card--front">
    <div class="stitch" style="top:8px"></div>
    <div class="stitch" style="top:58px"></div>
    <div class="front-band">
      <div class="stitch" style="top:8px"></div>
      <div class="stitch" style="top:322px"></div>
    </div>
    <div class="stitch" style="top:445px"></div>
    <div class="emblem-tab"></div>
    <div class="emblem emblem--front"></div>

    <div class="contact-panel">
      <div class="stitch" style="top:20px"></div>
      <div class="stitch" style="top:232px"></div>
      <div class="contact-row" style="top:44px">
        <svg width="24" height="22" viewBox="0 0 24 22"><rect x="1" y="4" width="22" height="17" rx="2" fill="var(--cream)"/><rect x="9" y="1" width="6" height="5" fill="var(--cream)"/><circle cx="8" cy="11" r="3" fill="var(--charcoal)"/><path d="M3 19c1-4 9-4 10 0z" fill="var(--charcoal)"/><rect x="15" y="10" width="6" height="2" fill="var(--charcoal)"/><rect x="15" y="14" width="6" height="2" fill="var(--charcoal)"/></svg>
        <div>Address // 5/22 Marlow Street<br>Ashgrove Queensland 4060 Australia</div>
      </div>
      <div class="contact-row" style="top:98px">
        <svg width="24" height="30" viewBox="0 0 24 30"><path d="M7 2c2 0 4 6 3 7l-3 2c1 4 4 9 7 11l3-2c1-1 6 3 6 5 0 2-3 4-5 4C9 28 2 16 3 6c0-2 2-4 4-4z" fill="var(--cream)"/></svg>
        <div style="margin-top:6px">Telephone nr. // 0493 215 764</div>
      </div>
      <div class="contact-row" style="top:148px">
        <svg width="26" height="18" viewBox="0 0 26 18"><rect x="1" y="1" width="24" height="16" fill="var(--cream)"/><path d="M1 1l12 9 12-9" fill="none" stroke="var(--charcoal)" stroke-width="1.5"/></svg>
        <div>E-Mail // <span class="email">lunetaduo@corvanet.com</span></div>
      </div>
      <div class="site-pill">website</div>
      <div class="site-url">www.<span>lunetaswingduo</span>.com</div>
    </div>

    <div class="tagline" style="top:142px">Perfect Live Music for Private &amp; Corporate Events</div>
    <div class="tagline" style="top:194px">Weddings and Dinner Music</div>
    <div class="wordmark wordmark--front">LUNETA DUO</div>

    <div class="ribbon" style="left:434px;top:282px;width:240px;height:42px">
      <svg width="240" height="42" viewBox="0 0 240 42"><path d="M0 8h20v30H0l8-15z" fill="var(--cream-shade)"/><path d="M240 8h-20v30h20l-8-15z" fill="var(--cream-shade)"/><rect x="12" y="2" width="216" height="32" fill="var(--cream)"/></svg>
      <div class="ribbon-text" style="top:2px;font-size:16px;line-height:32px;transform:scaleY(1.3)">CLASSIC COCKTAIL MUSIC</div>
    </div>

    <div class="members">Deborah Feltham /PIANO<br>Owen Lockett / BASS</div>
    <div class="instrument-art" role="img" aria-label="White illustration of a double bass with a piano keyboard along its neck"></div>
  </section>

  <section class="card card--back">
    <div class="stitch" style="top:26px"></div>
    <div class="stitch" style="top:36px"></div>
    <div class="stitch" style="top:430px"></div>
    <div class="stitch" style="top:440px"></div>
    <div class="emblem emblem--back"></div>
    <div class="wordmark wordmark--back">LUNETA DUO</div>

    <div class="ribbon" style="left:222px;top:294px;width:340px;height:90px">
      <svg width="340" height="90" viewBox="0 0 340 90"><path d="M0 18h40v62H0l14-31z" fill="var(--cream-shade)"/><path d="M340 18h-40v62h40l-14-31z" fill="var(--cream-shade)"/><path d="M28 68l12 12V68z" fill="var(--ribbon-fold)"/><path d="M312 68l-12 12V68z" fill="var(--ribbon-fold)"/><rect x="28" y="4" width="284" height="64" fill="var(--cream)"/></svg>
      <div class="ribbon-text" style="top:4px;font-size:22px;line-height:64px;transform:scaleY(1.6)">CLASSIC COCKTAIL MUSIC</div>
    </div>
  </section>

</div>
</body>
</html>
```